Social Media Post Quote #4 - Native American Organization

- KINDLER - must be included
- Protect your community. Protect Your Elders. Stay Vaccinated. must be included
- Attached, company Logo, campaign logos and sample flu social media image. - our audience likes BRIGHT colors.
- Must include image from the United States, representing Land/Nature from one of the following regions, Plains and Woodlands, or Southwest, or Mountains, or Coast.
- must include quote: Our wisdom carries through generations.
- One image will be provided twice - incorporating campaign logos - in some fashion
Inspiration: https://torvelink.org/ and https://www.facebook.com/Torvelink

```html
<!DOCTYPE html>
<html lang="en">
<head>
<meta charset="utf-8">
<title>KINDLER – Our wisdom carries through generations</title>
<link rel="stylesheet" href="https://fonts.googleapis.com/css2?family=Barlow:wght@500;600;700&family=Barlow+Semi+Condensed:wght@500;600&display=swap">
<style>
  :root {
    --rust: #b8584a;
    --teal: #3ea6b0;
    --rock-dark: #3b1d12;
    --rock-mid: #8a4526;
    --rock-light: #c0703a;
    --panel: rgba(238, 232, 225, 0.72);
    --header: rgba(246, 243, 239, 0.94);
  }
  * { margin: 0; padding: 0; box-sizing: border-box; }
  html, body { width: 1200px; height: 1200px; overflow: hidden; }
  body { font-family: "Barlow", sans-serif; }

  .post {
    position: relative;
    width: 1200px;
    height: 1200px;
    overflow: hidden;
  }
  .landscape-photo {
    position: absolute;
    inset: 0;
    background:
      radial-gradient(ellipse at 20% 80%, rgba(192,112,58,0.55), transparent 55%),
      radial-gradient(ellipse at 85% 20%, rgba(160,80,40,0.5), transparent 50%),
      linear-gradient(135deg, var(--rock-mid) 0%, var(--rock-dark) 45%, var(--rock-light) 75%, var(--rock-dark) 100%);
  }
  .quote-panel {
    position: absolute;
    left: 112px; top: 108px;
    width: 980px; height: 1005px;
    background: var(--panel);
    box-shadow: 0 4px 18px rgba(0,0,0,0.35);
  }
  .campaign-header {
    position: absolute;
    left: 147px; top: 147px;
    width: 915px; height: 311px;
    background: var(--header);
    box-shadow: 0 3px 10px rgba(0,0,0,0.25);
  }
  .campaign-title {
    position: absolute;
    left: 20px; top: 38px;
    width: 575px;
    text-align: center;
  }
  .campaign-name {
    font-family: "Barlow", sans-serif;
    font-weight: 500;
    font-size: 104px;
    line-height: 1;
    letter-spacing: 4px;
    color: var(--teal);
  }
  .campaign-subtitle {
    margin-top: 14px;
    font-family: "Barlow Semi Condensed", sans-serif;
    font-weight: 600;
    font-size: 24px;
    letter-spacing: 1.5px;
    line-height: 1;
    color: var(--rust);
  }
  .org-mark {
    position: absolute;
    left: 645px; top: 55px;
    width: 245px;
    text-align: center;
  }
  .org-dot {
    display: block;
    width: 64px; height: 64px;
    margin: 0 auto 14px;
    border-radius: 50%;
    background: var(--teal);
  }
  .org-name {
    font-family: "Barlow", sans-serif;
    font-weight: 600;
    font-size: 24px;
    line-height: 1.1;
    color: var(--rust);
    text-transform: uppercase;
  }
  .campaign-tagline {
    position: absolute;
    left: 0; right: 0; top: 238px;
    text-align: center;
    font-family: "Barlow Semi Condensed", sans-serif;
    font-weight: 500;
    font-size: 30px;
    color: var(--teal);
    letter-spacing: 0.5px;
  }
  .quote {
    position: absolute;
    left: 112px; top: 570px;
    width: 980px;
    text-align: center;
    font-family: "Barlow", sans-serif;
    font-weight: 700;
    line-height: 1;
    text-shadow: 3px 4px 6px rgba(40, 20, 10, 0.55);
  }
  .quote-line { display: block; }
  .quote-line--rust { color: var(--rust); font-size: 160px; letter-spacing: 2px; }
  .quote-line--teal { color: var(--teal); font-size: 124px; margin: 2px 0 8px; }
  .quote-line--last { font-size: 138px; letter-spacing: 1px; }
</style>
</head>
<body>
  <main class="post">
    <div class="landscape-photo" role="img" aria-label="Close-up of red Southwest sandstone rock face with ancient petroglyph carvings"></div>

    <div class="quote-panel"></div>

    <header class="campaign-header">
      <div class="campaign-title">
        <div class="campaign-name">KINDLER</div>
        <div class="campaign-subtitle">COVID -19 &amp; FLU VACCINATION CAMPAIGN</div>
      </div>
      <div class="org-mark">
        <span class="org-dot"></span>
        <div class="org-name">Torvelink<br>Elder Network</div>
      </div>
      <p class="campaign-tagline">Protect your community. Protect Your Elders. Stay Vaccinated.</p>
    </header>

    <h1 class="quote">
      <span class="quote-line quote-line--rust">Our wisdom</span>
      <span class="quote-line quote-line--teal">carries through</span>
      <span class="quote-line quote-line--rust quote-line--last">generations.</span>
    </h1>
  </main>
</body>
</html>
```